Top Real Estate teams new cards UPDATED

New Cards with MY (Im the tall guy in the middle) new pic on the front of card and my team pic on the back of card. Also my team name on the front of the card (marlow and partners) and brokerage name on the back (harborline real estate group) . Also the tag line "Ask about our 20 step plan" on the back of the card and "Welcome to the new way of Real Estate Sales" on the front of the card along with my phone number (951-284-7310) and email address (devon.marlow47@quillmail.net) my website (www.DevonMarlow.org) and my License number (BRE:07315942). I do like my team name colors of black and gold
Logo links are attached:
1. https://www.filecrate.net/sh/918kqwz72pavdle/AAF7QmR2HtK4BnYwPzLxUe_KGb?dl=0
2. https://www.filecrate.net/sh/27w5xvn81rbt094/AACKTJMR46DnQ2Wf7RyGs8Vh3b?dl=0
Updates

Target Market(s)

Real Estate Customers

Industry/Entity Type

Real Estate

Contact Information for Business Card

Classy, yet east ro read and understand

Font styles to use
Sans Serif

Requirements
Must have
• Team and brokerage name, and both slogans.
• Black and gold color scheme.
Nice to have
• Bold writing
Should not have
• cluttered feeling

```html
<!DOCTYPE html>
<html lang="en">
<head>
<meta charset="utf-8">
<title>Marlow and Partners – Business Card</title>
<link rel="stylesheet" href="https://fonts.googleapis.com/css2?family=Mulish:wght@400;600;700;800&display=swap">
<style>
  :root {
    --page: #e9e6e1;
    --ink: #111111;
    --black-soft: #1c1c1c;
    --gold: #f2d34a;
    --gold-light: #fbe98a;
    --gold-deep: #c9992e;
    --bronze: #8a5a1e;
    --bronze-dark: #4a2c0c;
    --rust: #7a2e14;
    --white: #ffffff;
    --text-dark: #2b1a06;
  }
  * { margin: 0; padding: 0; box-sizing: border-box; }
  html, body { width: 1200px; height: 1200px; overflow: hidden; }
  body {
    background: var(--page);
    font-family: "Mulish", sans-serif;
    position: relative;
  }
  .card {
    position: absolute;
    left: 100px;
    width: 1000px;
    height: 500px;
    overflow: hidden;
    box-shadow: 0 6px 18px rgba(0,0,0,0.18);
  }
  .card--front { top: 70px; background: var(--black-soft); }
  .card--back { top: 630px; background: var(--white); }
  .card__art { position: absolute; inset: 0; width: 100%; height: 100%; }

  /* front */
  .agent-photo {
    position: absolute; left: 58px; top: 22px; width: 130px; height: 448px;
    background: linear-gradient(180deg, #3a3a3a 0%, #141414 60%, #0b0b0b 100%);
    border-radius: 60px 60px 10px 10px;
  }
  .team-name {
    position: absolute; right: 108px; top: 58px;
    font-size: 54px; font-weight: 800; color: var(--ink); letter-spacing: 0.5px;
  }
  .welcome {
    position: absolute; left: 206px; top: 166px;
    font-size: 32px; font-weight: 800; color: var(--gold);
  }
  .front-tagline {
    position: absolute; right: 108px; top: 173px;
    font-size: 24px; font-weight: 600; color: var(--ink);
  }
  .contact {
    position: absolute; left: 260px; width: 600px; top: 268px;
    list-style: none; text-align: center;
    font-size: 28px; line-height: 38px; color: var(--text-dark);
  }

  /* back */
  .brokerage-mark {
    position: absolute; left: 70px; top: 96px;
    display: flex; align-items: center; gap: 12px;
    font-size: 40px; font-weight: 400; color: var(--ink);
  }
  .brokerage-mark__square { width: 16px; height: 16px; background: var(--ink); }
  .team-photo {
    position: absolute; left: 600px; top: 36px; width: 330px; height: 430px;
    background: linear-gradient(180deg, #4a4038 0%, #1a1a1a 45%, #0d0d0d 100%);
    border-radius: 80px 80px 20px 20px;
  }
  .brokerage-band__name {
    position: absolute; left: 46px; top: 322px;
    font-size: 46px; font-weight: 800; color: var(--gold); letter-spacing: 1px;
  }
  .brokerage-band__group {
    position: absolute; left: 436px; top: 322px;
    font-size: 48px; font-weight: 800; color: var(--ink); letter-spacing: 1px;
  }
  .back-tagline {
    position: absolute; left: 30px; top: 406px;
    font-size: 29px; font-weight: 400; color: var(--ink);
  }
</style>
</head>
<body>

<section class="card card--front">
  <svg class="card__art" viewBox="0 0 1000 500" preserveAspectRatio="none" aria-hidden="true">
    <defs>
      <linearGradient id="goldPanel" x1="0" y1="0" x2="1" y2="1">
        <stop offset="0" stop-color="#fbe98a"/>
        <stop offset="0.5" stop-color="#f2d34a"/>
        <stop offset="1" stop-color="#e9c23b"/>
      </linearGradient>
      <linearGradient id="bronzeBand" x1="0" y1="0" x2="0" y2="1">
        <stop offset="0" stop-color="#e0b24a"/>
        <stop offset="0.35" stop-color="#b07d2a"/>
        <stop offset="0.75" stop-color="#7a4e18"/>
        <stop offset="1" stop-color="#4a2c0c"/>
      </linearGradient>
    </defs>
    <rect width="1000" height="500" fill="#1c1c1c"/>
    <polygon points="200,0 925,0 925,232 432,232" fill="url(#goldPanel)"/>
    <rect x="0" y="246" width="925" height="199" fill="url(#bronzeBand)"/>
    <rect x="0" y="244" width="925" height="3" fill="#fbe98a"/>
    <rect x="0" y="442" width="925" height="4" fill="#f4c870"/>
    <polygon points="690,446 925,446 925,500 730,500" fill="#7a2e14"/>
    <rect x="925" y="0" width="75" height="500" fill="#0b0b0b"/>
  </svg>
  <div class="agent-photo" role="img" aria-label="Portrait of the agent standing in a black suit"></div>
  <h1 class="team-name">marlow and partners</h1>
  <p class="welcome">Welcome</p>
  <p class="front-tagline">to the new way of Real Estate Sales</p>
  <ul class="contact">
    <li>phone no. : 951-284-7310</li>
    <li>devon.marlow47@quillmail.net</li>
    <li>BRE:07315942</li>
    <li>www.DevonMarlow.org</li>
  </ul>
</section>

<section class="card card--back">
  <div class="brokerage-mark">
    <span class="brokerage-mark__square"></span>
    <span>Harborline</span>
  </div>
  <div class="team-photo" role="img" aria-label="Team photo of three agents in black outfits"></div>
  <svg class="card__art" viewBox="0 0 1000 500" preserveAspectRatio="none" aria-hidden="true">
    <defs>
      <linearGradient id="goldBand" x1="0" y1="0" x2="1" y2="1">
        <stop offset="0" stop-color="#f2d34a"/>
        <stop offset="0.5" stop-color="#fbe98a"/>
        <stop offset="1" stop-color="#f2d34a"/>
      </linearGradient>
    </defs>
    <polygon points="316,302 1000,302 1000,399 418,399" fill="url(#goldBand)"/>
    <polygon points="0,302 316,302 418,399 0,399" fill="#1c1c1c"/>
  </svg>
  <p class="brokerage-band__name">HARBORLINE</p>
  <p class="brokerage-band__group">REAL ESTATE GROUP</p>
  <p class="back-tagline">Ask about our 20 step plan</p>
</section>

</body>
</html>
```